Visitenkarte und Briefdesign
Zielgruppe
Limousinenservice (Stretchlimousinen)
Aufgabenstellung
Ich benötige eine Visitenkarte und ein Briefdesign in einer edlen Optik.
Auf folgender Seite können Informationen oder Bilder eingeholt werden
www.fahrt-glanzwerk.com
Ich mag einen Hintergrund in einer Lederoptik,( wie das Logo in Anhang, BILD x4)

```html
<!DOCTYPE html>
<html lang="de">
<head>
<meta charset="utf-8">
<title>RM NOBLECARS – Geschäftsausstattung</title>
<link href="https://fonts.googleapis.com/css2?family=Fira+Sans+Condensed:wght@400;600;700&family=Crimson+Text&display=swap" rel="stylesheet">
<style>
:root{
  --ink:#111;
  --leather-a:#2a2a2a;
  --leather-b:#050505;
  --gold:#c9a227;
  --grey:#9a9a9a;
  --footer:#a8a8a8;
  --paper:#fff;
  --page:#fff;
}
*{margin:0;padding:0;box-sizing:border-box}
html,body{width:1200px;height:955px;overflow:hidden;background:var(--page)}
body{position:relative;font-family:"Fira Sans Condensed",Arial,sans-serif;color:var(--ink)}
.leather{background:radial-gradient(ellipse at 60% 40%,var(--leather-a),var(--leather-b) 80%)}
.brand-mark{display:flex;align-items:center;justify-content:center;gap:6px;color:#bdbdbd;font-weight:700;letter-spacing:.5px}
.brand-mark .dot{width:9px;height:9px;border-radius:50%;background:#bdbdbd}

/* Briefbogen */
.letter{position:absolute;left:44px;top:32px;width:636px;height:898px;background:var(--paper);box-shadow:0 0 18px rgba(0,0,0,.35)}
.letter-head{position:absolute;left:0;top:0;width:100%;height:139px;border-top:4px solid var(--gold)}
.letter-head .title{position:absolute;left:60px;top:50px;color:#fff;font-size:21px;letter-spacing:.3px}
.title b{font-weight:700;margin-left:8px}
.letter-head .owner{position:absolute;left:60px;top:78px;color:var(--grey);font-size:13px}
.letter-head .brand-mark{position:absolute;left:420px;top:50px;width:150px;font-size:14px}
.sender-line{position:absolute;left:60px;top:160px;font-size:9.5px}
.sender-line b{font-weight:600;margin-right:8px}
.recipient{position:absolute;left:60px;top:192px;font-family:"Crimson Text",Georgia,serif;font-size:15px;line-height:19px}
.info{position:absolute;left:458px;top:161px;font-size:9.5px;line-height:12px}
.info h4{font-size:9.5px;font-weight:700;margin-top:12px}
.info .muted{color:var(--grey)}
.subject{position:absolute;left:60px;top:342px;font-size:12.5px;font-weight:700}
.date{position:absolute;left:458px;top:342px;font-size:10.5px}
.body-text{position:absolute;left:60px;top:390px;font-size:12px;line-height:18px}
.body-text p{position:absolute;left:0;white-space:nowrap}
.letter-foot{position:absolute;left:40px;top:825px;right:20px;font-size:7.6px;line-height:11.5px;color:var(--footer)}
.letter-foot div{position:absolute;top:0;white-space:nowrap}
.letter-base{position:absolute;left:0;bottom:0;width:100%;height:7px;background:var(--ink)}

/* Visitenkarte Vorderseite */
.card{position:absolute;left:745px;width:414px;height:266px;box-shadow:0 0 14px rgba(0,0,0,.35);background:var(--paper)}
.card-front{top:194px}
.card-front .frame{position:absolute;inset:7px;border:2px solid var(--gold)}
.card-front .brand-mark{position:absolute;inset:0;font-size:24px}
.card-front .brand-mark .dot{width:14px;height:14px}

/* Visitenkarte Rückseite */
.card-back{top:492px}
.card-back .band{position:absolute;left:0;top:0;width:100%;height:68px;border-top:4px solid var(--gold)}
.card-back .title{position:absolute;left:22px;top:24px;color:#fff;font-size:18px}
.card-back .brand-mark{position:absolute;left:320px;top:22px;width:90px;font-size:10px}
.card-back .brand-mark .dot{width:6px;height:6px}
.person{position:absolute;left:22px;top:86px;font-size:14px;font-weight:700}
.role{position:absolute;left:22px;top:104px;font-size:11px;color:#bbb}
.col{position:absolute;top:148px;font-size:11.5px;line-height:15px}
.col h4{font-size:11.5px;font-weight:700}
.col .muted{color:#aaa}
.card-back .base{position:absolute;left:0;bottom:0;width:100%;height:7px;background:var(--ink)}
</style>
</head>
<body>

<section class="letter">
  <header class="letter-head leather" role="img" aria-label="Schwarzer Lederhintergrund">
    <div class="title">LIMOUSINENSERVICE<b>RM NOBLECARS</b></div>
    <div class="owner">Inhaber Jorven Kalder</div>
    <div class="brand-mark"><span class="dot"></span>RM NOBLECARS</div>
  </header>

  <div class="sender-line"><b>Limousinenservice RM NOBLECARS</b>Lindenweg 42 B &nbsp;&nbsp; 46399 Falkenau</div>

  <address class="recipient" style="font-style:normal">Max Mustermann<br>Musterstraße 12<br>12121 Musterhausen</address>

  <div class="info">
    Lindenweg 42 B<br>46399 Falkenau
    <h4>E-Mail</h4>info@rm-noblecars.de
    <h4>Telefon</h4>0170 555 48 21<br><span class="muted">(24 Stunden erreichbar)</span>
    <h4>Web</h4>www.fahrt-glanzwerk.com<br>www.rm-noblecars.de
  </div>

  <div class="subject">Betreff</div>
  <div class="date">Datum</div>

  <div class="body-text">
    <p style="top:0">Sehr geehrte Damen und Herren,</p>
    <p style="top:38px">[hier folgt der Text]</p>
    <p style="top:110px">[noch eine weitere Anmerkung]</p>
    <p style="top:163px">[nun folgt der Schlusssatz]</p>
    <p style="top:219px">Mit freundlichen Grüßen</p>
    <p style="top:237px">Jorven Kalder</p>
  </div>

  <footer class="letter-foot">
    <div style="left:0">LIMOUSINENSERVICE RM NOBLECARS<br>Lindenweg 42 B<br>46399 Falkenau</div>
    <div style="left:117px">Tel<br>Mail<br>Web</div>
    <div style="left:141px">0170 555 48 21<br>info@rm-noblecars.de<br>www.rm-noblecars.de</div>
    <div style="left:212px">Amtsgericht Falkenau<br>HBR XXXXX<br>USt-ID-Nr. DEXXXXXXX</div>
    <div style="left:300px">Geschäftsführung und<br>Inhaber:<br>Jorven Kalder</div>
    <div style="left:386px">Bankname<br>Konto: XXXXXXX<br>BLZ: XXX XXX XXX</div>
    <div style="left:455px">IBAN: DEXXXX XXXX XXXX XXXX<br>BIC: XXXXXXXXX<br>www.fahrt-glanzwerk.com</div>
  </footer>
  <div class="letter-base"></div>
</section>

<section class="card card-front leather" role="img" aria-label="Schwarzer Lederhintergrund mit Firmenname">
  <div class="frame"></div>
  <div class="brand-mark"><span class="dot"></span>RM NOBLECARS</div>
</section>

<section class="card card-back">
  <header class="band leather" role="img" aria-label="Schwarzer Lederhintergrund">
    <div class="title">LIMOUSINENSERVICE<b>RM NOBLECARS</b></div>
    <div class="brand-mark"><span class="dot"></span>RM NOBLECARS</div>
  </header>
  <div class="person">JORVEN KALDER</div>
  <div class="role">Inhaber</div>
  <div class="col" style="left:22px">Lindenweg 42 B<br>46399 Falkenau</div>
  <div class="col" style="left:161px"><h4>E-Mail</h4>info@rm-noblecars.de<h4 style="margin-top:12px">Telefon</h4>0170 555 48 21<br><span class="muted">(24 Stunden erreichbar)</span></div>
  <div class="col" style="left:289px"><h4>Web</h4>www.fahrt-glanzwerk.com<br>www.rm-noblecars.de</div>
  <div class="base"></div>
</section>

</body>
</html>
```